"Show Times" Poster for Stunt Show

I need a fairly simple 24"x 36" poster made. I'm a professional mountain bike stunt rider and I need a poster to put on a sandwich board to display my showtimes for people walking by. The top of the poster will say: Mountain Bike (Trials) Stunt Show This text will be centered at the top BUT I want the "(Trials)" to be slightly crooked and a bit opaque with a stamped-looking font and overlap the other words just slightly. Hopefully that makes sense. Somewhere in the middle will be a photoshopped picture of me doing a stunt on my bike. The bottom will have a blank white space titled, "Show Times:" that I can write my showtimes inside of. I've attached a wildly crude and poor drawing of the basic concept. Remember, this is for a stunt show so it must look cool and have some rad colors and design... but also be simple. I will provide a picture of myself riding to be used in the poster. It will take up the middle third.

Target Market(s)

Families, Parents, Kids, general public, mountain bike enthusiastss

Industry/Entity Type

Entertainment Industry

Font styles to use
Sans Serif

Colors

Designer to choose colors to be used in the design.

Requirements
Must have
• A blank, rectangular, white space on the bottom for Show times Labelled "Show Times:"
Nice to have
• I'd like background of the whole poster to be relatively black with cool subtle graphics.

```html
<!DOCTYPE html>
<html lang="en">
<head>
<meta charset="UTF-8">
<title>Mountain Bike Stunt Show – Show Times</title>
<link href="https://fonts.googleapis.com/css2?family=Lilita+One&family=Bitter:ital,wght@1,800&display=swap" rel="stylesheet">
<style>
  :root {
    --brand-blue: #2a64d1;
    --deep-blue: #1f4fb0;
    --paper: #ffffff;
    --photo-dark: #4b4f55;
    --photo-light: #c9ccd0;
  }
  html, body {
    margin: 0;
    padding: 0;
    overflow: hidden;
    background: var(--paper);
  }
  .poster {
    position: relative;
    width: 800px;
    height: 1200px;
    background: var(--paper);
    overflow: hidden;
  }
  .title {
    position: absolute;
    left: 0;
    width: 100%;
    margin: 0;
    font-family: "Lilita One", sans-serif;
    font-weight: 400;
    color: var(--brand-blue);
    text-align: center;
    font-size: 82px;
    line-height: 1;
    letter-spacing: 1px;
  }
  .title-line-1 { top: 28px; }
  .title-line-2 { top: 106px; left: -70px; }
  .title-stamp {
    position: absolute;
    left: 470px;
    top: 118px;
    font-family: "Lilita One", sans-serif;
    font-size: 58px;
    color: var(--paper);
    -webkit-text-stroke: 4px var(--brand-blue);
    paint-order: stroke fill;
    transform: rotate(-4deg);
    opacity: 0.92;
    letter-spacing: 1px;
  }
  .hero {
    position: absolute;
    left: 0;
    top: 0;
    width: 800px;
    height: 1200px;
  }
  .showtimes-band {
    position: absolute;
    left: 0;
    top: 893px;
    width: 800px;
    height: 66px;
    background: var(--brand-blue);
    box-shadow: 0 -8px 0 -5px var(--brand-blue), 0 8px 0 -5px var(--brand-blue);
  }
  .showtimes-band::before,
  .showtimes-band::after {
    content: "";
    position: absolute;
    left: 0;
    width: 100%;
    height: 3px;
    background: var(--brand-blue);
  }
  .showtimes-band::before { top: -10px; }
  .showtimes-band::after { bottom: -10px; }
  .showtimes-label {
    margin: 0;
    padding-left: 176px;
    font-family: "Bitter", serif;
    font-style: italic;
    font-weight: 800;
    font-size: 46px;
    line-height: 66px;
    color: var(--paper);
    letter-spacing: 1px;
  }
  .showtimes-space {
    position: absolute;
    left: 0;
    top: 975px;
    width: 800px;
    height: 210px;
    background: var(--paper);
  }
  .footer-rule {
    position: absolute;
    left: 0;
    top: 1188px;
    width: 800px;
    height: 5px;
    background: var(--brand-blue);
  }
</style>
</head>
<body>
<main class="poster">
  <svg class="hero" viewBox="0 0 800 1200" xmlns="http://www.w3.org/2000/svg">
    <defs>
      <linearGradient id="photoTone" x1="0" y1="0" x2="0" y2="1">
        <stop offset="0" stop-color="var(--photo-light)"/>
        <stop offset="0.55" stop-color="#8d9196"/>
        <stop offset="1" stop-color="var(--photo-dark)"/>
      </linearGradient>
    </defs>
    <polygon class="hero-band-top" points="0,234 800,252 800,272 0,252" fill="var(--brand-blue)"/>
    <polygon class="hero-photo" role="img" aria-label="Photo of a trials rider in a helmet balancing a mountain bike on its rear wheel on top of a table, spectators watching inside an arena hall"
      points="0,250 800,268 800,796 0,856" fill="url(#photoTone)"/>
    <polygon class="hero-band-bottom" points="440,830 800,796 800,830 520,860" fill="var(--brand-blue)"/>
  </svg>

  <h1 class="title title-line-1">Mountain Bike</h1>
  <p class="title title-line-2">Stunt Show</p>
  <span class="title-stamp">(TRIALS)</span>

  <section class="showtimes-band">
    <h2 class="showtimes-label">SHOW TIMES :</h2>
  </section>
  <div class="showtimes-space"></div>
  <div class="footer-rule"></div>
</main>
</body>
</html>
```